Advertisement Design

I'm looking for a post card sized advertisement piece that I will be dropping off to commercial and residential customers.
On one side I want it promoting carpet cleaning services and on the other side dryer vent cleaning services.
I've uploaded two different layouts of my company logo for you to choice from.
One batch will be printed with my Michigan Number
One batch will be printed with my Tennessee number
Will share contact numbers with the winner so just use a make up number
555-319-4826

Slow in providing feedback

```html
<!DOCTYPE html>
<html lang="en">
<head>
<meta charset="utf-8">
<title>Loom Ranger – Postcards</title>
<link href="https://fonts.googleapis.com/css2?family=Montserrat:wght@400;500;700;800&display=swap" rel="stylesheet">
<style>
  :root{
    --blue:#1f80c6;
    --blue-deep:#1a5dad;
    --blue-light:#7dc7f3;
    --charcoal:#4a4a4d;
    --grey-arc:#9a9a9d;
    --white:#ffffff;
    --stage-top:#6a6665;
    --stage-bottom:#8a8786;
  }
  *{box-sizing:border-box;margin:0;padding:0}
  html,body{width:1113px;height:1200px;overflow:hidden}
  body{background:linear-gradient(var(--stage-top),var(--stage-bottom));font-family:'Montserrat',Arial,sans-serif}
  .canvas{position:relative;width:1113px;height:1200px;overflow:hidden}
  .postcard{position:absolute;left:170px;width:773px;height:551px;overflow:hidden;box-shadow:0 12px 24px rgba(0,0,0,.35);background:var(--white)}
  .postcard--dryer{top:33px}
  .postcard--carpet{top:617px}
  .postcard__art{position:absolute;inset:0;width:773px;height:551px}
  .brand{position:absolute;left:40px;top:24px;width:230px;text-align:center}
  .brand__mark{display:block;width:60px;height:60px;margin:0 auto 10px;background:var(--blue)}
  .brand__name{display:block;white-space:nowrap;font-weight:500;font-size:25px;line-height:30px;letter-spacing:1px;color:var(--blue-deep)}
  .headline{position:absolute;left:37px;color:var(--white);font-weight:800;line-height:1.02}
  .postcard--dryer .headline{top:210px;font-size:33px}
  .postcard--carpet .headline{top:193px;font-size:42px}
  .intro{position:absolute;left:37px;color:var(--white);font-size:14.2px;line-height:18.5px;font-weight:400}
  .postcard--dryer .intro{top:292px;width:370px}
  .postcard--carpet .intro{top:292px;width:370px}
  .checklist{position:absolute;list-style:none;color:var(--white);font-weight:700;font-size:15.5px;line-height:24.5px}
  .checklist li{position:relative;padding-left:22px}
  .checklist li::before{content:"";position:absolute;left:0;top:5px;width:13px;height:13px;border:1.6px solid var(--white);border-radius:50%}
  .checklist li::after{content:"";position:absolute;left:4.5px;top:8px;width:3px;height:6px;border:solid var(--white);border-width:0 1.6px 1.6px 0;transform:rotate(45deg)}
  .postcard--dryer .checklist{left:37px;top:401px}
  .checklist--left{left:37px;top:380px}
  .checklist--right{left:347px;top:388px;line-height:20px}
  .checklist--right li{margin-bottom:4px}
  .checklist--right li::before{top:3px}
  .checklist--right li::after{top:6px}
  .photo-label{position:absolute;color:var(--white);font-size:13px;font-weight:500}
  .footer-tag{position:absolute;left:0;top:497px;width:300px;height:54px;display:flex;align-items:center;justify-content:center;text-align:center;color:var(--blue-deep);font-weight:500;font-size:15.5px;line-height:19px}
  .footer-quote{position:absolute;left:330px;top:505px;color:var(--blue-light);font-weight:500;font-size:15.5px;line-height:19px;text-align:center}
  .footer-rule{position:absolute;left:481px;top:504px;width:1.5px;height:40px;background:var(--white)}
  .footer-call{position:absolute;left:493px;top:500px;color:var(--white);font-weight:700;font-size:23.5px;letter-spacing:.5px}
  .footer-web{position:absolute;left:512px;top:528px;color:var(--white);font-size:14px;letter-spacing:.3px}
  .footer-web::before{content:"";position:absolute;left:-15px;top:4px;width:10px;height:10px;border:1.4px solid var(--white);border-radius:50%}
  .seal-text{font-family:'Montserrat',Arial,sans-serif;font-weight:800;fill:var(--white)}
</style>
</head>
<body>
<main class="canvas">

  <!-- Dryer vent side -->
  <section class="postcard postcard--dryer">
    <svg class="postcard__art" viewBox="0 0 773 551" xmlns="http://www.w3.org/2000/svg">
      <defs>
        <linearGradient id="dryerPhoto" x1="0" y1="0" x2="1" y2="1">
          <stop offset="0" stop-color="#a8623a"/>
          <stop offset=".45" stop-color="#8fa9c4"/>
          <stop offset="1" stop-color="#c9c6c2"/>
        </linearGradient>
        <radialGradient id="ductBefore"><stop offset="0" stop-color="#2a2420"/><stop offset="1" stop-color="#6c5a4c"/></radialGradient>
        <radialGradient id="ductAfter"><stop offset="0" stop-color="#3a3c3f"/><stop offset="1" stop-color="#a7aaad"/></radialGradient>
        <path id="sealTopD" d="M298 205 A44 44 0 0 1 386 205"/>
        <path id="sealBotD" d="M290 205 A52 52 0 0 0 394 205"/>
      </defs>
      <path class="band-edge" d="M0 170 C130 150 260 155 340 195" fill="none" stroke="var(--charcoal)" stroke-width="10"/>
      <path class="blue-band" d="M0 178 C130 158 260 163 345 205 C400 235 440 275 500 300 L773 300 L773 497 L0 497 Z" fill="var(--blue)"/>
      <path role="img" aria-label="Photo of a technician cleaning a dryer duct with a blue air mover" d="M335 0 L773 0 L773 300 L470 300 C390 265 320 160 335 0 Z" fill="url(#dryerPhoto)"/>
      <path d="M325 0 C312 160 385 270 465 305" fill="none" stroke="var(--grey-arc)" stroke-width="9"/>
      <circle role="img" aria-label="Clogged dryer duct before cleaning" cx="497" cy="305" r="80" fill="url(#ductBefore)" stroke="var(--white)" stroke-width="6"/>
      <circle role="img" aria-label="Clean dryer duct after cleaning" cx="674" cy="305" r="80" fill="url(#ductAfter)" stroke="var(--white)" stroke-width="6"/>
      <g class="seal">
        <circle cx="342" cy="205" r="66" fill="var(--blue)"/>
        <circle cx="342" cy="205" r="60" fill="var(--charcoal)" stroke="var(--white)" stroke-width="3"/>
        <circle cx="342" cy="205" r="32" fill="var(--white)" stroke="var(--blue)" stroke-width="4"/>
        <text class="seal-text" font-size="14"><textPath href="#sealTopD" startOffset="50%" text-anchor="middle">SATISFACTION</textPath></text>
        <text class="seal-text" font-size="14"><textPath href="#sealBotD" startOffset="50%" text-anchor="middle">GUARANTEED</textPath></text>
        <text x="342" y="199" text-anchor="middle" font-size="9" fill="var(--blue)">★ ★ ★</text>
        <text x="340" y="220" text-anchor="middle" font-family="Montserrat,Arial,sans-serif" font-weight="800" font-size="22" fill="var(--blue)">100<tspan font-size="9">%</tspan></text>
      </g>
      <path d="M300 497 L773 497 L773 551 L300 551 Z" fill="var(--blue-deep)"/>
    </svg>
    <div class="brand"><span class="brand__mark"></span><span class="brand__name">LOOM RANGER</span></div>
    <h2 class="headline">DRYER VENT<br>CLEANING</h2>
    <p class="intro">Professional dryer duct cleaning from Loom Ranger can help your dryer work at peak efficiency, which can save money on energy bills. A clean dryer duct also makes your home safer by helping prevent dryer firesand, for gas dryers.</p>
    <ul class="checklist">
      <li>PROFESSIONELLY INSPECT</li>
      <li>EXCELLENT STANDARDS</li>
      <li>GUARANTEE TO REMOVE ALL THE LINT</li>
    </ul>
    <span class="photo-label" style="left:457px;top:451px">BEFORE</span>
    <span class="photo-label" style="left:663px;top:454px">AFTER</span>
    <p class="footer-tag">RESIDENTIAL &amp; COMMERCIAL<br>CLEANING SERVICES</p>
    <p class="footer-quote">GET YOUR FREE<br>QUOTE TODAY !</p>
    <span class="footer-rule"></span>
    <p class="footer-call">CALL &nbsp;(555) 274-0193</p>
    <p class="footer-web">WWW.LOOMRANGER.COM</p>
  </section>

  <!-- Carpet cleaning side -->
  <section class="postcard postcard--carpet">
    <svg class="postcard__art" viewBox="0 0 773 551" xmlns="http://www.w3.org/2000/svg">
      <defs>
        <linearGradient id="carpetPhoto" x1="0" y1="0" x2="0" y2="1">
          <stop offset="0" stop-color="#e4e2de"/>
          <stop offset=".4" stop-color="#bcbab6"/>
          <stop offset=".55" stop-color="#2f8fa6"/>
          <stop offset="1" stop-color="#2aa0b8"/>
        </linearGradient>
        <radialGradient id="rugTone"><stop offset="0" stop-color="#e7e2d8"/><stop offset="1" stop-color="#7b7a80"/></radialGradient>
        <radialGradient id="sofaTone"><stop offset="0" stop-color="#6b6a70"/><stop offset="1" stop-color="#2d2b30"/></radialGradient>
        <radialGradient id="creamTone"><stop offset="0" stop-color="#f1ede4"/><stop offset="1" stop-color="#c9c1b2"/></radialGradient>
        <path id="sealTopC" d="M651 413 A36 36 0 0 1 723 413"/>
        <path id="sealBotC" d="M644 413 A43 43 0 0 0 730 413"/>
      </defs>
      <path d="M0 170 C110 150 230 150 310 175" fill="none" stroke="var(--charcoal)" stroke-width="10"/>
      <path class="blue-band" d="M0 178 C110 158 230 158 320 185 L773 260 L773 497 L0 497 Z" fill="var(--blue)"/>
      <path role="img" aria-label="Photo of a carpet extractor cleaning a teal rug" d="M335 0 L773 0 L773 345 C740 300 690 255 620 220 C520 175 400 120 335 0 Z" fill="url(#carpetPhoto)"/>
      <path d="M322 0 C380 130 520 185 620 228 C690 258 745 305 773 355" fill="none" stroke="var(--grey-arc)" stroke-width="9"/>
      <circle role="img" aria-label="Technician cleaning a rug fringe" cx="347" cy="183" r="80" fill="url(#rugTone)" stroke="var(--white)" stroke-width="6"/>
      <circle role="img" aria-label="Upholstery cleaning on a dark sofa" cx="497" cy="303" r="80" fill="url(#sofaTone)" stroke="var(--white)" stroke-width="6"/>
      <circle role="img" aria-label="Extractor wand on a cream carpet" cx="672" cy="283" r="80" fill="url(#creamTone)" stroke="var(--white)" stroke-width="6"/>
      <g class="seal">
        <circle cx="687" cy="413" r="56" fill="var(--blue)"/>
        <circle cx="687" cy="413" r="50" fill="var(--charcoal)" stroke="var(--white)" stroke-width="3"/>
        <circle cx="687" cy="413" r="26" fill="var(--white)" stroke="var(--blue)" stroke-width="3.5"/>
        <text class="seal-text" font-size="11.5"><textPath href="#sealTopC" startOffset="50%" text-anchor="middle">SATISFACTION</textPath></text>
        <text class="seal-text" font-size="11.5"><textPath href="#sealBotC" startOffset="50%" text-anchor="middle">GUARANTEED</textPath></text>
        <text x="687" y="408" text-anchor="middle" font-size="7.5" fill="var(--blue)">★ ★ ★</text>
        <text x="685" y="426" text-anchor="middle" font-family="Montserrat,Arial,sans-serif" font-weight="800" font-size="18" fill="var(--blue)">100<tspan font-size="7.5">%</tspan></text>
      </g>
      <path d="M300 497 L773 497 L773 551 L300 551 Z" fill="var(--blue-deep)"/>
    </svg>
    <div class="brand"><span class="brand__mark"></span><span class="brand__name">LOOM RANGER</span></div>
    <h2 class="headline">CARPET<br>CLEANING</h2>
    <p class="intro">We have been providing Carpet Cleaning Services for 40 years. With state-of-the-art industrial equipment &amp; out years of experience there is not mush we cannot get clean.</p>
    <ul class="checklist checklist--left">
      <li>RUG CLEANING</li>
      <li>BLEACH REPAIR</li>
      <li>UPHOLSTERY CLEANING</li>
      <li>PET STAIN AND SCENT REMOVAL</li>
    </ul>
    <ul class="checklist checklist--right">
      <li>BOAT, RV, PRIVATE PLANE<br>CARPET CLEANING</li>
      <li>CORRIDOR &amp; OUTDOOR<br>CARPET CLEANING</li>
    </ul>
    <p class="footer-tag">RESIDENTIAL &amp; COMMERCIAL<br>CLEANING SERVICES</p>
    <p class="footer-quote">GET YOUR FREE<br>QUOTE TODAY !</p>
    <span class="footer-rule"></span>
    <p class="footer-call">CALL &nbsp;(555) 274-0193</p>
    <p class="footer-web">WWW.LOOMRANGER.COM</p>
  </section>

</main>
</body>
</html>
```